New letter head for Air Conditioning business

We need a new professional letter head design to suit our new re-branded air conditioning business. Our new logo is attached

```html
<!DOCTYPE html>
<html lang="en">
<head>
<meta charset="utf-8">
<title>Norvane Letterhead</title>
<link rel="stylesheet" href="https://fonts.googleapis.com/css2?family=Open+Sans:wght@400;600;700&display=swap">
<style>
  :root {
    --backdrop: #e4e4e6;
    --paper: #ffffff;
    --ink: #2b2b2b;
    --ink-soft: #555555;
    --coral: #ec5a4d;
    --charcoal: #232323;
    --mint: #cfe6d6;
    --green: #3fae5b;
    --signature-tone: #e9ebf2;
  }
  * { box-sizing: border-box; margin: 0; padding: 0; }
  html, body { width: 1200px; height: 795px; overflow: hidden; }
  body {
    background: var(--backdrop);
    font-family: "Open Sans", Arial, sans-serif;
    color: var(--ink);
    position: relative;
  }
  .letterhead {
    position: absolute;
    left: 330px; top: 16px;
    width: 540px; height: 764px;
    background: var(--paper);
    box-shadow: 0 2px 10px rgba(0,0,0,.12);
    overflow: hidden;
  }
  .header-art {
    position: absolute; left: 0; top: 92px;
    width: 540px; height: 44px;
    background: linear-gradient(100deg, var(--mint) 0%, #f3c6c0 45%, var(--coral) 80%, var(--charcoal) 100%);
    opacity: .55;
  }
  .brand {
    position: absolute; right: 34px; top: 34px;
    display: flex; align-items: center; gap: 8px;
  }
  .brand-dot { width: 16px; height: 16px; border-radius: 50%; background: var(--green); }
  .brand-name { font-size: 20px; font-weight: 700; letter-spacing: 3px; color: var(--charcoal); }
  .letter-body {
    position: absolute; left: 48px; top: 188px; width: 300px;
    font-size: 7.4px; line-height: 1.45; color: var(--ink-soft);
  }
  .date { margin-bottom: 12px; color: var(--ink); font-size: 8px; }
  .recipient { font-weight: 600; color: var(--ink); font-size: 8px; line-height: 1.35; margin-bottom: 10px; }
  .salutation { font-weight: 700; color: var(--ink); font-size: 9px; margin-bottom: 12px; }
  .letter-body p.para { margin-bottom: 11px; }
  .sign-off {
    position: absolute; right: 46px; top: 300px; width: 130px;
    font-size: 8px; color: var(--ink); text-align: right;
  }
  .signature {
    display: block; width: 96px; height: 24px; margin: 8px 0 6px auto;
    background: linear-gradient(90deg, var(--signature-tone), #f5f6fa);
    border-radius: 3px;
  }
  .sign-off .name { line-height: 1.35; }
  .contact {
    position: absolute; right: 34px; bottom: 74px;
    text-align: right; font-size: 7px; font-weight: 600; color: var(--ink); line-height: 1.7;
  }
  .contact-row { display: flex; justify-content: flex-end; align-items: center; gap: 4px; }
  .contact-row svg { width: 8px; height: 8px; }
  .web { color: var(--coral); font-weight: 700; }
</style>
</head>
<body>
  <main class="letterhead">
    <div class="header-art" role="img" aria-label="Decorative header wave in mint, coral and charcoal tones"></div>

    <div class="brand">
      <span class="brand-dot"></span>
      <span class="brand-name">NORVANE</span>
    </div>

    <section class="letter-body">
      <p class="date">January 03, 2017</p>
      <p class="recipient">Mr. John Doe<br>President<br>AA Corporation<br>111 Street Name, Suite#<br>City, State, 12345</p>
      <p class="salutation">Dear Mr. John,</p>
      <p class="para">Lorem Ipsum is simply dummy text of the printing and typesetting industry. Lorem Ipsum has been the industry's standard dummy text ever since the 1500s, when an unknown printer took a galley of type and scrambled it to make a type specimen book. It has survived not only five centuries, but also the leap into electronic typesetting, remaining essentially unchanged.</p>
      <p class="para">The standard chunk of Lorem Ipsum used since the 1500s is reproduced below for those interested. Sections 1.10.32 and 1.10.33 from "de Finibus Bonorum et Malorum" by Cicero are also reproduced in their exact original form, accompanied by English versions from the 1914 translation by H. Rackham.</p>
      <p class="para">Lorem Ipsum is simply dummy text of the printing and typesetting industry. Lorem Ipsum has been the industry's standard dummy text ever since the 1500s, when an unknown printer took a galley of type and scrambled it to make a type specimen book. It has survived not only five centuries, but also the leap into electronic typesetting, remaining essentially unchanged. It was popularised in the</p>
    </section>

    <aside class="sign-off">
      <p>Sincerely Your,</p>
      <span class="signature" role="img" aria-label="Handwritten signature"></span>
      <p class="name">Name Last Name<br>Company Name</p>
    </aside>

    <footer class="contact">
      <p>SUITE 102 STREET NAME, STATE, ZIP 2024, COUNTRY</p>
      <div class="contact-row">
        <svg viewBox="0 0 10 10" aria-hidden="true"><circle cx="5" cy="5" r="5" fill="var(--green)"/><path d="M3 2.5l1 1-.5.8a4 4 0 0 0 2.2 2.2l.8-.5 1 1-.7.8C5 7.5 2.5 5 2.3 3.2z" fill="#fff"/></svg>
        <span>(00) 01234 567 890</span>
        <svg viewBox="0 0 10 10" aria-hidden="true"><circle cx="5" cy="5" r="5" fill="var(--green)"/><path d="M3 2.5l1 1-.5.8a4 4 0 0 0 2.2 2.2l.8-.5 1 1-.7.8C5 7.5 2.5 5 2.3 3.2z" fill="#fff"/></svg>
        <span>(00) 01234 567 891</span>
        <svg viewBox="0 0 10 10" aria-hidden="true"><circle cx="5" cy="5" r="5" fill="var(--green)"/><rect x="2.5" y="3.2" width="5" height="3.6" fill="#fff"/><path d="M2.5 3.2L5 5.3 7.5 3.2" stroke="var(--green)" stroke-width=".6" fill="none"/></svg>
        <span>hello@norvaneair.com</span>
      </div>
      <p class="web">www.norvaneair.com</p>
    </footer>
  </main>
</body>
</html>
```